Digital content business needs banner ads

We sell content - if you need an article to put on your website or in a newsletter, you can purchase a ready made article from us and edit it to your liking to use straight away. This could be any kind of article, but this banner ad will be aimed at real estate agents. You can see the website (and the style of articles) here https://www.thecopperwrenpost.com.au
The banner is meant to solve the problem of the front desk admin or agent trying to think of something to write to put in their email newsletter. This will save them time as they can just select an article from our library and use it (for a fee of course!).
Needs to have the words:
--------------------------------------------------
Find the next article for your newsletter
---------------------------------------------------
Some imagery would be good rather than plain text.
With a call to action like click here button or similar
Required sizes (or provide a set of standard sized ads):
728 x 90
970 x 250
300x250
Target Market(s)
Real Estate Agents

```html
<!DOCTYPE html>
<html lang="en">
<head>
<meta charset="utf-8">
<title>Find The Next Article For Your Newsletter – The Copper Wren Post</title>
<link rel="stylesheet" href="https://fonts.googleapis.com/css2?family=Poppins:wght@600;700&display=swap">
<style>
  :root {
    --sky-pale: #dce8fd;
    --sky-light: #b9d0fb;
    --sky-mid: #8fb3f6;
    --blue-deep: #4f83ee;
    --blue-bright: #3a6fe8;
    --white: #ffffff;
    --cta-gold: #f7b324;
    --cta-ink: #2b3a87;
    --brand-ink: #1f4fd1;
  }
  * { margin: 0; padding: 0; box-sizing: border-box; }
  html, body { width: 1200px; height: 148px; overflow: hidden; background: var(--sky-pale); }
  .banner {
    position: relative;
    width: 1200px;
    height: 148px;
    overflow: hidden;
    font-family: "Poppins", Arial, sans-serif;
    background: var(--sky-pale);
  }
  .banner__backdrop { position: absolute; inset: 0; }
  .banner__illustration {
    position: absolute;
    left: 30px;
    top: 8px;
    width: 340px;
    height: 134px;
    border-radius: 18px;
    background: linear-gradient(135deg, #e9f0fe 0%, #c6d9fb 55%, #9fbff7 100%);
  }
  .banner__message {
    position: absolute;
    left: 470px;
    top: 18px;
    width: 440px;
    text-align: center;
    color: var(--white);
    font-weight: 600;
    font-size: 25px;
    line-height: 37px;
    letter-spacing: 0.3px;
  }
  .banner__cta {
    position: absolute;
    left: 552px;
    top: 94px;
    width: 276px;
    height: 34px;
    border-radius: 8px;
    background: var(--cta-gold);
    color: var(--cta-ink);
    font-weight: 600;
    font-size: 20px;
    line-height: 34px;
    text-align: center;
    text-decoration: none;
  }
  .brand {
    position: absolute;
    left: 968px;
    top: 34px;
    width: 210px;
    display: flex;
    align-items: center;
    gap: 10px;
    text-decoration: none;
  }
  .brand__mark {
    flex: 0 0 auto;
    width: 26px;
    height: 26px;
    border-radius: 50%;
    background: var(--brand-ink);
  }
  .brand__name {
    color: var(--brand-ink);
    font-weight: 700;
    font-size: 21px;
    line-height: 26px;
  }
</style>
</head>
<body>
  <div class="banner">
    <svg class="banner__backdrop" width="1200" height="148" viewBox="0 0 1200 148" aria-hidden="true">
      <path d="M250 0 H1000 C960 40 990 90 940 148 H230 C300 110 210 60 250 0 Z" fill="var(--sky-mid)"/>
      <path d="M330 0 H930 C880 50 930 100 880 148 H380 C430 110 300 60 330 0 Z" fill="var(--blue-deep)"/>
      <path d="M700 148 C760 110 830 120 880 148 Z" fill="var(--blue-bright)" opacity="0.6"/>
      <path d="M980 0 H1200 V148 H1010 C1060 100 940 60 980 0 Z" fill="var(--sky-light)" opacity="0.5"/>
    </svg>

    <div class="banner__illustration" role="img" aria-label="Illustration of a person pulling an article from a laptop screen, with papers, a coffee cup and a plant"></div>

    <h1 class="banner__message">Find The Next Article<br>For Your Newsletter</h1>

    <a class="banner__cta" href="https://www.thecopperwrenpost.com.au">Check It Now!</a>

    <a class="brand" href="https://www.thecopperwrenpost.com.au">
      <span class="brand__mark" aria-hidden="true"></span>
      <span class="brand__name">The Copper Wren Post</span>
    </a>
  </div>
</body>
</html>
```